Bathroom Remodeling Guide Needed

We need to create a Bathroom remodeling guide that we can give away as a freemium download. The attached file contains the instructions and copy for the guide along with our logo. Below is a dropbox link to our assets folder as well.

https://www.filevaultora.net/sh/fo/k7trw2mzq9plv804bxnhe/QJTmVzaPwErKs5yUxLcHoBn4?key=7hfpt2c9048rwq1ma5517j39m&dl=0

```html
<!DOCTYPE html>
<html lang="en">
<head>
<meta charset="UTF-8">
<title>Bathroom Remodeling Guide – Planning</title>
<link rel="stylesheet" href="https://fonts.googleapis.com/css2?family=Cormorant+Garamond:wght@700&family=Lato:ital,wght@0,300;0,400;1,300&display=swap">
<style>
  :root {
    --page-bg: #f2f2f2;
    --panel-bg: #d6cec3;
    --heading: #2b2b2b;
    --body: #3f3f3f;
    --quote: #857c72;
    --gold: #c8a877;
    --divider: #dcbcb3;
    --frame: #5a5550;
  }
  html, body {
    margin: 0;
    padding: 0;
    width: 1200px;
    height: 927px;
    overflow: hidden;
  }
  .page {
    position: relative;
    width: 1200px;
    height: 927px;
    background: var(--page-bg);
    font-family: "Lato", sans-serif;
    font-weight: 300;
    color: var(--body);
  }
  .page-title {
    position: absolute;
    left: 62px;
    top: 112px;
    margin: 0;
    width: 840px;
    font-family: "Cormorant Garamond", serif;
    font-weight: 700;
    font-size: 73px;
    line-height: 87px;
    color: var(--heading);
    white-space: nowrap;
  }
  .title-rule {
    position: absolute;
    left: 63px;
    top: 431px;
    width: 823px;
    height: 3px;
    background: var(--gold);
  }
  .intro {
    position: absolute;
    left: 68px;
    top: 460px;
    width: 255px;
    font-size: 22.5px;
    line-height: 27px;
  }
  .intro p { margin: 0 0 27px; }
  .column-divider {
    position: absolute;
    left: 370px;
    top: 450px;
    width: 2px;
    height: 420px;
    background: var(--divider);
  }
  .requirements {
    position: absolute;
    left: 441px;
    top: 460px;
    width: 405px;
    font-size: 22.5px;
    line-height: 27px;
  }
  .requirements p { margin: 0 0 27px; }
  .label { text-transform: uppercase; }
  .checklist {
    list-style: none;
    margin: 0 0 27px;
    padding: 0 0 0 14px;
  }
  .checklist li {
    position: relative;
    padding-left: 17px;
  }
  .checklist li svg {
    position: absolute;
    left: 0;
    top: 10px;
  }
  .quote-panel {
    position: absolute;
    left: 932px;
    top: 0;
    width: 268px;
    height: 927px;
    background: var(--panel-bg);
  }
  .pull-quote {
    position: absolute;
    left: 50px;
    top: 145px;
    margin: 0;
    font-style: italic;
    font-weight: 300;
    font-size: 36px;
    line-height: 64.5px;
    color: var(--quote);
    white-space: nowrap;
  }
  .page-number {
    position: absolute;
    left: 220px;
    top: 881px;
    width: 32px;
    height: 33px;
    border-left: 1.5px solid var(--frame);
    border-right: 1.5px solid var(--frame);
    box-sizing: border-box;
    font-size: 22px;
    line-height: 33px;
    text-align: center;
    color: #3a3734;
    font-weight: 400;
  }
</style>
</head>
<body>
<main class="page">
  <h1 class="page-title">Most Bathroom<br>Remodels Go Wrong<br>Before They Even Start</h1>
  <div class="title-rule"></div>

  <section class="intro">
    <p>The success of a bathroom remodel is determined long before construction begins.</p>
    <p>The most common mistake homeowners make is starting without a clear, well-thought-out plan. Decisions are made on the fly, materials are selected too late, and small issues quickly turn into costly problems.</p>
  </section>

  <div class="column-divider"></div>

  <section class="requirements">
    <div class="label">A successful project requires:</div>
    <ul class="checklist">
      <li><svg width="10" height="10" viewBox="0 0 10 10"><path d="M1 5 L4 8 L9 1" fill="none" stroke="#c8a877" stroke-width="2"/><rect x="0.5" y="0.5" width="9" height="9" fill="none" stroke="#c8a877" stroke-width="1"/></svg>A clear design vision</li>
      <li><svg width="10" height="10" viewBox="0 0 10 10"><path d="M1 5 L4 8 L9 1" fill="none" stroke="#c8a877" stroke-width="2"/><rect x="0.5" y="0.5" width="9" height="9" fill="none" stroke="#c8a877" stroke-width="1"/></svg>Thoughtful material selection</li>
      <li><svg width="10" height="10" viewBox="0 0 10 10"><path d="M1 5 L4 8 L9 1" fill="none" stroke="#c8a877" stroke-width="2"/><rect x="0.5" y="0.5" width="9" height="9" fill="none" stroke="#c8a877" stroke-width="1"/></svg>Proper planning before demolition</li>
      <li><svg width="10" height="10" viewBox="0 0 10 10"><path d="M1 5 L4 8 L9 1" fill="none" stroke="#c8a877" stroke-width="2"/><rect x="0.5" y="0.5" width="9" height="9" fill="none" stroke="#c8a877" stroke-width="1"/></svg>A team that understands both design and construction</li>
    </ul>
    <p><span class="label">When these elements are in place,</span><br>the process becomes smooth, predictable, and even enjoyable.</p>
    <p><span class="label">When they’re not,</span><br>the experience is often the opposite.</p>
  </section>

  <aside class="quote-panel">
    <blockquote class="pull-quote">“The biggest<br>mistake<br>homeowners<br>make is<br>starting<br>without<br>a clear<br>plan.”</blockquote>
    <div class="page-number">2</div>
  </aside>
</main>
</body>
</html>
```